KWI Business Card

Please create a creative design for a business card using the new theme from the Logo & website. This company's main focus is food manufacturing building construction. Please integrate the new logo attached.

Please use the following information for the demo card:

Korvel Walls, Inc.
Dana Whitcombe
dwhitcombe@korvelwalls.example
Cell: 312-555-0178
218 Larkmoor Ave
Alderbrook, KS 60418

See pictures and more information on the website.

www.korvelwalls.example

```html
<!DOCTYPE html>
<html lang="en">
<head>
<meta charset="utf-8">
<title>KWI Business Card</title>
<link href="https://fonts.googleapis.com/css2?family=Josefin+Sans:wght@300;400;600&display=swap" rel="stylesheet">
<style>
  :root {
    --bg: #e4e4e6;
    --paper: #f6f6f7;
    --blue-deep: #3f6fae;
    --blue-mid: #5f8ec6;
    --blue-light: #a9c5e4;
    --ink-black: #0c0c0c;
    --text-light: #eef3fa;
    --logo-blue: #3e6aa6;
    --logo-blue-back: #2f5690;
  }
  * { box-sizing: border-box; margin: 0; padding: 0; }
  html, body { width: 1200px; height: 801px; overflow: hidden; }
  body {
    background: var(--bg);
    font-family: "Josefin Sans", sans-serif;
    position: relative;
  }
  .card {
    position: absolute;
    width: 530px;
    height: 303px;
    border-radius: 3px;
    overflow: hidden;
    box-shadow: 0 6px 18px rgba(0,0,0,0.12);
  }
  /* Front */
  .card--front { left: 45px; top: 110px; background: var(--paper); }
  .front__band {
    position: absolute; left: 0; right: 0; bottom: 0; height: 168px;
    background: linear-gradient(90deg, var(--blue-deep) 0%, var(--blue-mid) 60%, var(--blue-light) 100%);
  }
  .front__corner {
    position: absolute; right: 0; top: 0; width: 108px; height: 135px;
    background: var(--ink-black);
  }
  .front__badge {
    position: absolute; right: 46px; top: 70px; width: 120px; height: 120px;
    border-radius: 50%;
    background: radial-gradient(circle, #f4f8fd 0%, #dfe9f6 55%, #b8cfea 100%);
  }
  .brand {
    position: absolute; left: 28px; top: 42px;
    display: flex; align-items: center; gap: 10px;
    color: var(--logo-blue); font-weight: 600; font-size: 26px;
  }
  .brand__mark { width: 18px; height: 18px; background: var(--logo-blue); }
  .front__name {
    position: absolute; left: 28px; top: 158px;
    color: var(--text-light); font-weight: 400; font-size: 21px; letter-spacing: 1.5px;
    text-transform: uppercase;
  }
  .contact {
    position: absolute; left: 28px; top: 196px;
    list-style: none; color: var(--text-light); font-weight: 300; font-size: 13.5px;
  }
  .contact li { display: flex; align-items: center; gap: 9px; height: 24px; }
  .contact svg { width: 14px; height: 14px; flex: none; }
  .address {
    position: absolute; left: 320px; top: 196px;
    color: var(--text-light); font-weight: 300; font-size: 14px; line-height: 24px;
    font-style: normal;
  }
  /* Back */
  .card--back {
    left: 625px; top: 388px;
    background: linear-gradient(160deg, var(--blue-light) 0%, var(--blue-mid) 45%, var(--blue-deep) 100%);
  }
  .back__brand {
    position: absolute; inset: 0;
    display: flex; align-items: center; justify-content: center; gap: 14px;
    color: var(--logo-blue-back); font-weight: 600; font-size: 34px;
  }
  .back__brand .brand__mark { width: 24px; height: 24px; background: var(--logo-blue-back); }
</style>
</head>
<body>
  <section class="card card--front" aria-label="Business card front">
    <div class="front__band"></div>
    <div class="front__corner"></div>
    <div class="front__badge" role="img" aria-label="Snowflake emblem"></div>
    <div class="brand"><span class="brand__mark"></span><span>Korvel Walls, Inc.</span></div>
    <h1 class="front__name">Dana Whitcombe</h1>
    <ul class="contact">
      <li>
        <svg viewBox="0 0 16 16"><circle cx="8" cy="8" r="8" fill="#eef3fa"/><path d="M5 4.5l1.6-.4 1 2-1 .8a5 5 0 0 0 2.5 2.5l.8-1 2 1-.4 1.6c-3.5.3-6.8-3-6.5-6.5z" fill="#3f6fae"/></svg>
        <span>312-555-0178</span>
      </li>
      <li>
        <svg viewBox="0 0 16 16"><circle cx="8" cy="8" r="8" fill="#eef3fa"/><rect x="4" y="5" width="8" height="6" fill="none" stroke="#3f6fae" stroke-width="1.2"/><path d="M4 5l4 3.5L12 5" fill="none" stroke="#3f6fae" stroke-width="1.2"/></svg>
        <span>dwhitcombe@korvelwalls.example</span>
      </li>
      <li>
        <svg viewBox="0 0 16 16"><circle cx="8" cy="8" r="8" fill="#eef3fa"/><circle cx="8" cy="8" r="4.2" fill="none" stroke="#3f6fae" stroke-width="1.1"/><path d="M3.8 8h8.4M8 3.8c-2 2.4-2 6 0 8.4M8 3.8c2 2.4 2 6 0 8.4" fill="none" stroke="#3f6fae" stroke-width="1"/></svg>
        <span>www.korvelwalls.example</span>
      </li>
    </ul>
    <address class="address">218 Larkmoor Ave<br>Alderbrook, KS 60418</address>
  </section>

  <section class="card card--back" role="img" aria-label="Business card back: blue field with faint snowflake pattern">
    <div class="back__brand"><span class="brand__mark"></span><span>Korvel Walls, Inc.</span></div>
  </section>
</body>
</html>
```